Testing form re-design

I have 2 new testing forms in a very basic format, I need them updated to look similar to our other testing forms. Attached are the two new forms (Dermatology and GI) as well as a couple of our Original normal testing forms to compare them to. Needs to be in an editable PSD file incase I need to change the verbiage in the future. Also a few addendums to the Dermatology form - Need to add a form field for "Clinical Impression" as well as "Clinical History" with spaces 2 inches to handwrite next to them.

Industry/Entity Type

Healthcare

Font styles to use
Sans Serif

Colors

Designer to choose colors to be used in the design.

Requirements
Must have
• All the information on the current forms

```html
<!DOCTYPE html>
<html lang="en">
<head>
<meta charset="utf-8">
<title>Gastrointestinal Test Requisition Form</title>
<link href="https://fonts.googleapis.com/css2?family=Roboto:ital,wght@0,400;0,500;0,700;1,700&family=Roboto+Condensed:wght@700&display=swap" rel="stylesheet">
<style>
:root{
  --navy:#1d3c78;
  --blue:#2f63b0;
  --bar:#e4ebf5;
  --line:#7d8798;
  --ink:#1b1f27;
  --muted:#4a5160;
  --red:#d0262b;
  --paper:#ffffff;
}
*{box-sizing:border-box;margin:0;padding:0}
html,body{width:729px;height:1200px;overflow:hidden;background:var(--paper)}
body{font-family:"Roboto",Arial,sans-serif;color:var(--ink);font-size:6px;line-height:1.25;position:relative}
.req{color:var(--red);font-weight:400}
.abs{position:absolute}

/* header */
.brand{left:10px;top:10px;display:flex;align-items:center;gap:5px}
.brand-dot{width:26px;height:26px;border-radius:50%;background:var(--navy)}
.brand-name{font-weight:700;font-size:11px;color:var(--navy);line-height:1;width:60px}
.title{left:0;width:729px;top:10px;text-align:center}
.title h1{font-family:"Roboto Condensed",Arial,sans-serif;font-size:17px;color:var(--navy);letter-spacing:.2px}
.title .addr{font-size:10px;font-weight:700;color:var(--ink);margin-top:1px}
.title .contact{font-size:9px;color:var(--ink);margin-top:3px;font-weight:500}
.badge{right:10px;top:8px;width:74px;height:30px;border-radius:4px;background:#c9d6ea}

/* boxes */
.box{border:1px solid var(--line)}
.bar{background:var(--bar);border-bottom:1px solid var(--line);text-align:center;font-weight:700;font-size:8px;padding:1px 0}
.note{color:var(--red);font-size:5px;padding:2px 4px;text-align:center}
.field{border-bottom:1px solid var(--line);padding:1px 3px;height:13px;font-size:5.5px}
.row{display:flex}
.row>.field{flex:1;border-right:1px solid var(--line)}
.row>.field:last-child{border-right:none}
.cb{display:inline-block;width:5px;height:5px;border:.7px solid var(--ink);margin-right:2px;vertical-align:-1px}

/* left column */
.order{left:8px;top:62px;width:250px;height:176px}
.order .sig{position:absolute;left:0;right:0;bottom:0}
.biopsy{left:8px;top:242px;width:250px;height:470px}
.types{display:grid;grid-template-columns:1fr 1fr 1fr;padding:2px 4px;gap:1px 4px;font-size:5.5px}
.sect-label{font-weight:700;font-size:6px;padding:2px 4px 0}
.codes{display:grid;grid-template-columns:repeat(3,1fr);padding:1px 4px 3px;gap:0 4px;font-size:5.5px}
table{border-collapse:collapse;width:100%}
th,td{border:1px solid var(--line);font-size:5px;padding:1px 2px;text-align:center}
th{background:var(--bar);font-weight:700;height:22px}
td{height:19px}
td:first-child{font-weight:700;width:18px}
.stains{padding:3px 4px;font-size:5.5px}
.other{left:8px;top:716px;width:250px;height:88px}
.other-title{font-weight:700;font-size:12px;padding:2px 4px;color:var(--navy)}

/* right column */
.patient{left:262px;top:62px;width:459px;height:266px}
.choices{padding:2px 3px;border-bottom:1px solid var(--line);font-size:5.5px;min-height:13px}
.choices b{margin-right:3px}
.choices span{margin-right:5px;white-space:nowrap}
.billing{left:262px;top:330px;width:459px;height:56px}
.panel-title{left:262px;width:459px;top:390px;text-align:center;font-weight:700;font-size:20px;color:var(--navy)}
.panels{left:290px;top:418px;width:420px}
.panel{margin-bottom:7px}
.panel h3{font-size:8px;font-style:italic;font-weight:700;color:var(--navy);display:flex;align-items:center;gap:4px}
.panel h3 .cb{width:8px;height:8px;border-width:1px}
.panel ul{list-style:none;padding-left:22px;margin-top:1px}
.panel li{font-size:6px;line-height:1.35}
.panel li::before{content:"•";margin-right:4px;color:var(--navy)}
.panel .spec{font-size:6px;padding-left:22px}
.icd{left:262px;top:716px;width:459px;height:88px}
.icd-title{text-align:center;font-weight:700;font-size:9px;padding:2px}

/* legal */
.legal{left:8px;width:713px;font-size:5.2px;line-height:1.35;color:var(--muted);text-align:justify}
.legal h4{font-size:6.5px;color:var(--ink);margin-bottom:1px}
.legal p{margin-bottom:1px}
.sigline{left:420px;top:1184px;width:300px;border-top:1px solid var(--ink);font-size:6px;font-weight:700;padding-top:1px;display:flex;justify-content:space-between}
</style>
</head>
<body>

<header>
  <div class="abs brand"><span class="brand-dot"></span><span class="brand-name">RIVERBEND LABS</span></div>
  <div class="abs title">
    <h1>GASTROINTESTINAL TEST REQUISITION FORM</h1>
    <div class="addr">4120 Orchard Park Dr Suite 210, Lakeview, MI 48000</div>
    <div class="contact">(555) 014-2290 • www.riverbendlabs.example</div>
  </div>
  <div class="abs badge" aria-hidden="true"></div>
</header>

<section class="abs box order">
  <div class="bar">Ordering Physician/Laboratory</div>
  <div class="note">(Required: Include the ordering physician's first &amp; last name, NPI, practice name, complete address, phone number, and fax number.)</div>
  <div class="sig">
    <div class="field" style="border-top:1px solid var(--line)">Physician to receive additional result report:</div>
    <div class="row"><div class="field" style="flex:3">Physician's Signature</div><div class="field">Date</div></div>
  </div>
</section>

<section class="abs box biopsy">
  <div class="bar">Biopsy Information</div>
  <div class="field">ICD10 codes <span class="req">(required)</span></div>
  <div class="row">
    <div class="field" style="height:18px">Date Collected <span class="req">(required)</span></div>
    <div class="field" style="height:18px">Time Collected</div>
    <div class="field" style="height:18px">Collector Signature</div>
    <div class="field" style="height:18px">No. vials collected</div>
  </div>
  <div class="sect-label">Type:</div>
  <div class="types">
    <span><i class="cb"></i>Adenoma</span><span><i class="cb"></i>Crohn's</span><span><i class="cb"></i>H. pylori</span>
    <span><i class="cb"></i>Barrett's Esophagus</span><span><i class="cb"></i>Dysplasia</span><span><i class="cb"></i>Microscopic Colitis</span>
    <span><i class="cb"></i>Cancer</span><span><i class="cb"></i>Eosinophilic Esophagitis</span><span><i class="cb"></i>Polyp</span>
    <span><i class="cb"></i>Candida</span><span><i class="cb"></i>Gastritis</span><span><i class="cb"></i>Lymphoma</span>
    <span><i class="cb"></i>Colitis</span><span><i class="cb"></i>GERD</span><span><i class="cb"></i>Ulcer / Other</span>
  </div>
  <div class="sect-label">Endoscopic Finding Code:</div>
  <div class="codes">
    <span>1. Normal</span><span>7. Mass</span><span>13. Hemorrhoids</span>
    <span>2. Polyp</span><span>8. Friable</span><span>14. Diverticula</span>
    <span>3. Barrett's Mucosa</span><span>9. Hypertrophic</span><span>15. Inflamed Mucosa</span>
    <span>4. Erosion</span><span>10. Atrophic</span><span>16. Edematous</span>
    <span>5. Ulcer</span><span>11. Hemorrhagic</span><span>17. Granular</span>
    <span>6. Stricture</span><span>12. Nodular</span><span>18. Other</span>
  </div>
  <table>
    <tr><th colspan="2">Anatomic Site of Biopsy Container</th><th>Organ &amp; Site</th><th>Dimension (cm)</th><th>Endoscopic Finding (see codes above)</th></tr>
    <tr><td>A</td><td></td><td></td><td></td><td></td></tr>
    <tr><td>B</td><td></td><td></td><td></td><td></td></tr>
    <tr><td>C</td><td></td><td></td><td></td><td></td></tr>
    <tr><td>D</td><td></td><td></td><td></td><td></td></tr>
    <tr><td>E</td><td></td><td></td><td></td><td></td></tr>
    <tr><td>F</td><td></td><td></td><td></td><td></td></tr>
    <tr><td>G</td><td></td><td></td><td></td><td></td></tr>
    <tr><td>H</td><td></td><td></td><td></td><td></td></tr>
  </table>
  <div class="stains"><b>Special Stains For:</b><br>
    <i class="cb"></i>H. pylori &nbsp; <i class="cb"></i>Fungus &nbsp; <i class="cb"></i>TB &nbsp; <i class="cb"></i>Iron &nbsp; <i class="cb"></i>Other ________</div>
</section>

<section class="abs box other"><div class="other-title">Other Test/Panel</div></section>

<section class="abs box patient">
  <div class="bar">Patient Information (Please Print)</div>
  <div class="field">Name (Last, First) <span class="req">(required)</span></div>
  <div class="field">In Care of:</div>
  <div class="field">Patient Address</div>
  <div class="row"><div class="field" style="flex:3">City</div><div class="field">State</div><div class="field">Zip</div></div>
  <div class="row"><div class="field" style="height:16px">Date of Birth <span class="req">(Required)</span></div><div class="field" style="height:16px;flex:.6">Age</div><div class="field" style="height:16px">Sex <span class="req">(Required)</span> <i class="cb"></i>M <i class="cb"></i>F</div></div>
  <div class="row"><div class="field" style="height:16px;flex:2">Phone Number</div><div class="field" style="height:16px"><i class="cb"></i>Cell Phone<br><i class="cb"></i>Home Phone</div></div>
  <div class="choices"><b>Race:</b><span><i class="cb"></i>Native American / Alaskan</span><span><i class="cb"></i>Asian</span><span><i class="cb"></i>Black or African American</span><span><i class="cb"></i>White</span><span><i class="cb"></i>Multicultural</span><span><i class="cb"></i>Native Hawaiian / Pacific Islander</span><span><i class="cb"></i>Other</span><span><i class="cb"></i>Declined</span></div>
  <div class="choices"><b>Ethnicity:</b><span><i class="cb"></i>Hispanic or Latino</span><span><i class="cb"></i>Not Hispanic or Latino</span><span><i class="cb"></i>Do not wish to disclose</span><span><i class="cb"></i>Unknown</span></div>
  <div class="choices"><b>Gender Identity:</b><span><i class="cb"></i>Male</span><span><i class="cb"></i>Female</span><span><i class="cb"></i>Transgender</span><span><i class="cb"></i>Nonbinary</span><span><i class="cb"></i>Other</span><span><i class="cb"></i>Do not wish to disclose</span></div>
  <div class="choices"><b>Sexual Orientation:</b><span><i class="cb"></i>Straight</span><span><i class="cb"></i>Gay</span><span><i class="cb"></i>Lesbian</span><span><i class="cb"></i>Bisexual</span><span><i class="cb"></i>Something else</span><span><i class="cb"></i>Do not wish to disclose</span></div>
  <div class="field">Patient Email</div>
  <div class="field" style="border-bottom:none">Patient Signature</div>
</section>

<section class="abs box billing">
  <div class="bar">Billing Information (Please include a copy of the front &amp; back of card.)</div>
  <div class="choices"><b>Billing Type:</b><span><i class="cb"></i>Patient</span><span><i class="cb"></i>Insurance</span><span><i class="cb"></i>Physician/Client</span> &nbsp; <b>Relationship:</b><span><i class="cb"></i>Self</span><span><i class="cb"></i>Spouse</span><span><i class="cb"></i>Dependent</span></div>
  <div class="row"><div class="field">Primary Insurance Carrier</div><div class="field">Medicare / Medicaid or Policy ID#</div></div>
  <div class="row"><div class="field" style="border-bottom:none">Employer/Group Name</div><div class="field" style="border-bottom:none">Group#</div></div>
</section>

<div class="abs panel-title">GI Panel</div>

<section class="abs panels">
  <div class="panel">
    <h3><i class="cb"></i>PX Max Enteric Bacterial Panel</h3>
    <ul>
      <li>Salmonella spp.</li>
      <li>Campylobacter spp. (jejuni and coli)</li>
      <li>Shigella spp./Enteroinvasive E. coli (EIEC)</li>
      <li>Shiga toxin 1 (stx1) and Shiga toxin 2 (stx2)</li>
      <li>Vibrio (V. vulnificus, V. parahaemolyticus, and V. cholerae)</li>
      <li>Enterotoxigenic E. coli (ETEC)</li>
      <li>Yersinia enterocolitica</li>
    </ul>
    <div class="spec">Specimen Types: Unpreserved soft to diarrheal stool, Cary-Blair preserved stool</div>
  </div>
  <div class="panel">
    <h3><i class="cb"></i>PX Max Enteric Parasite Panel</h3>
    <ul><li>Giardia lamblia</li><li>Cryptosporidium (C. hominis and C. parvum)</li><li>Entamoeba histolytica</li></ul>
    <div class="spec">Specimen Types: Unpreserved soft to diarrheal stool, 10% Formalin fixed stool</div>
  </div>
  <div class="panel">
    <h3><i class="cb"></i>PX Max Enteric Viral Panel</h3>
    <ul><li>Norovirus GI/GII</li><li>Rotavirus A</li><li>Adenovirus F40/41</li><li>Sapovirus (genogroups I, II, IV, V)</li><li>Human Astrovirus (hAstV)</li></ul>
    <div class="spec">Specimen Types: Unpreserved soft to diarrheal stool, Cary-Blair preserved stool</div>
  </div>
  <div class="panel">
    <h3><i class="cb"></i>PX Max Cdiff Assay</h3>
    <ul><li>Clostridium difficile toxin B gene (tcdB)</li></ul>
    <div class="spec">Specimen Types: Unformed (liquid or soft) stool</div>
  </div>
</section>

<section class="abs box icd"><div class="icd-title">ICD10 codes <span class="req">(required)</span></div></section>

<section class="abs legal" style="top:810px">
  <h4>Physician Authorization</h4>
  <p>1. The undersigned healthcare provider acknowledges that when ordering a test, the laboratory will perform the services requested at the address above and that results will be reported only to the ordering provider and to the persons listed on this form. The provider confirms that the testing ordered is medically necessary for the diagnosis and treatment of the patient.</p>
  <p>2. I certify that I am the treating provider and that the information given on this form is accurate and complete to the best of my knowledge. I understand that specimens will be processed according to the standards of the laboratory and that additional testing may be performed to confirm results.</p>
  <p>3. I attest that the patient has been informed of the tests ordered and has agreed to the collection and submission of the specimen for analysis.</p>
  <p>4. I acknowledge that this referral process may affect billing procedures and timelines for results, and I accept the terms of the reporting and payment procedures for these specific test types.</p>
  <p>5. I confirm that I have informed my patients about the testing arrangement and that all records will be kept in keeping with the rules on patient privacy.</p>
</section>

<section class="abs legal" style="top:950px">
  <h4>Patient Consent and Authorization</h4>
  <p>I authorize the release of my medical information, including test results, for the purpose of obtaining payment for services performed by this laboratory. I assign any benefits to which I am entitled to be paid directly to the laboratory for the services provided. I understand that I am financially responsible for any amount not covered by my insurance, including deductibles, co-payments and charges for services that are not approved. I agree that a copy of this authorization shall be as valid as the original. I permit the laboratory to contact my insurance carrier on my behalf and to appeal any decision that denies payment for the tests ordered by my provider.</p>
  <p>I understand that my insurance plan may require a referral or prior approval and that the laboratory will make a reasonable effort to obtain it. If approval cannot be obtained, I may be contacted before testing proceeds. I consent to receive calls, texts and emails about my account and results at the numbers and addresses I have given. I understand that I may revoke this authorization in writing at any time, except to the extent that action has already been taken in reliance on it.</p>
  <p>Medicare patients: I request that payment of authorized benefits be made on my behalf to the laboratory for any services furnished to me. I authorize the holder of medical information about me to release to the program and its agents any information needed to determine these benefits. By signing this form, I acknowledge that I have read and understand the statements above and that my questions have been answered to my satisfaction.</p>
</section>

<div class="abs sigline"><span>Patient Signature</span><span>Date</span></div>

</body>
</html>
```